Spiral Bound Classy Marketing Planner Cover Design

A5 marketing planner book cover requiredClassy, minimalist design for female entrepreneurs. The inside is all in grey and is a minimalist uncluttered design. Name of the planner is It's Time Marketing Recipe PlannerHeader font inside the planner is Shelby and other font is Lato Brand colours are teal and grey.The printing format has changed and as such I am looking for a new cover design to make this marketing planner look classy and engaging. Would prefer my logo to be on the back. We have the option for a 10cm x 10cm foil detail to be added on the front cover, feel free to add this to your design.This is for a spiral bound book - A5 front cover and A5 back cover - no spine required.

Target Market(s)

Female entrepreneurs

Industry/Entity Type

Marketing

Colors
33b8a4
ffffff

Requirements
Must have
• Front and back designs
• A5
Should not have
• Large illustrations
• People in the design
• Spine design

```html
<!DOCTYPE html>
<html lang="en">
<head>
<meta charset="utf-8">
<title>Bright Path Promotion Blueprint Planner — Cover</title>
<link href="https://fonts.googleapis.com/css2?family=Bebas+Neue&family=Lato:ital,wght@0,400;0,700;0,900;1,400&family=Roboto+Condensed:wght@700&display=swap" rel="stylesheet">
<style>
  :root {
    --stage: #000000;
    --paper: #ffffff;
    --teal: #1ab7c1;
    --grey: #8c8c8c;
    --grey-dark: #5a5a5a;
    --grey-soft: #9a9a9a;
    --idea-yellow: #f3c43a;
    --idea-amber: #e9a825;
  }
  * { margin: 0; padding: 0; box-sizing: border-box; }
  html, body { width: 1199px; height: 1200px; overflow: hidden; background: var(--stage); }
  .stage { position: relative; width: 1199px; height: 1200px; }

  .side-label {
    position: absolute; top: 144px; width: 540px; text-align: center;
    font-family: "Lato", sans-serif; font-weight: 700; font-size: 33px;
    color: var(--grey-dark);
  }
  .side-label--back { left: 32px; }
  .side-label--front { left: 626px; }

  .cover {
    position: absolute; top: 219px; width: 540px; height: 762px;
    background: var(--paper); overflow: hidden;
  }
  .cover--back { left: 32px; }
  .cover--front { left: 626px; }

  /* Back cover */
  .brand-name {
    position: absolute; left: 0; top: 300px; width: 100%; text-align: center;
    font-family: "Lato", sans-serif; font-weight: 900; font-size: 46px;
    line-height: 1.1; color: var(--teal);
  }
  .brand-tagline {
    position: absolute; left: 137px; top: 532px; width: 266px;
    font-family: "Roboto Condensed", sans-serif; font-weight: 700;
    font-size: 16px; line-height: 21px; color: var(--grey);
    text-transform: uppercase;
  }
  .brand-tagline__line {
    display: block; white-space: nowrap; letter-spacing: 2.4px;
    text-align: justify; text-align-last: justify;
  }

  /* Front cover */
  .intro {
    position: absolute; top: 26px; left: 0; width: 100%; text-align: center;
    font-family: "Lato", sans-serif; font-style: italic; font-size: 18.5px;
    line-height: 23px; color: var(--grey-soft);
  }
  .title { position: absolute; left: 0; width: 100%; text-align: center;
    font-family: "Bebas Neue", sans-serif; font-weight: 400; color: var(--teal);
    line-height: 1; white-space: nowrap; }
  .title__kicker { top: 132px; font-size: 46px; letter-spacing: 0.5px; }
  .title__main { top: 190px; font-size: 138px; letter-spacing: 1px; }
  .title__sub { top: 326px; font-size: 146px; letter-spacing: 2px; }

  .idea-visual {
    position: absolute; left: 270px; top: 455px; width: 270px; height: 307px;
    background: radial-gradient(circle at 42% 40%, var(--idea-yellow) 0 16%, var(--idea-amber) 20%, rgba(243,196,58,0.15) 34%, var(--paper) 55%);
  }
</style>
</head>
<body>
<div class="stage">
  <div class="side-label side-label--back">back</div>
  <div class="side-label side-label--front">front</div>

  <section class="cover cover--back">
    <p class="brand-name">The Copper<br>Whisk</p>
    <p class="brand-tagline">
      <span class="brand-tagline__line">Planning with the clear</span>
      <span class="brand-tagline__line">Steps for steady growth</span>
    </p>
  </section>

  <section class="cover cover--front">
    <p class="intro">Lorem ipsum dolor sit amet, consectetuer<br>Lorem ipsum dolor sit amet, consectetuer</p>
    <h1>
      <span class="title title__kicker">Bright Path Promotion</span>
      <span class="title title__main">Blueprint</span>
      <span class="title title__sub">Planner</span>
    </h1>
    <div class="idea-visual" role="img" aria-label="Crumpled yellow paper ball forming a light bulb with a drawn cord and spark lines"></div>
  </section>
</div>
</body>
</html>
```